Marriage Retreat: 4 Page Color Brochure

I need a 4 page, full color brochure that is 8.5 x 11 when folded (11 x 17 front/back when printed/unfolded). The brochure is to inform pastors and religious leaders about a private retreat to help them strengthen their marriages. Attached you will find: (1) a Word document with the copy/text and initial guidelines on the page layout (although some flexibility on what text goes on which page is acceptable); (2) a creative brief PDF with some of the visual ideas I have to jumpstart your thinking; (3) logo files for the organization Brightwater Circle (the logo must be included); (4) original scan of tree artwork that can be used as a visual element (this is the same tree that has been converted to a vector file in the logo; please use a color scheme in the brochure that is complementary to this artwork). The overall feel for this piece should be timeless, classic, welcoming and approachable. The font in the logo is Audrey, although it has been stylized a bit. Please take that into account when selecting fonts for the layout. I do not yet have the photo of Tom & Norma (the hosts of this retreat) for you to include with their bios. Please insert a placeholder image for now and I will get you the actual photo in a few days. Once we get to the final stage, I would also like to have a version of the file that is laid out as 4 individual 8.5x11 pages so it can be printed in that format if needed. I would also like to have a PDF version of each file.

Target Market(s)

The initial target market for this type of service will be males (who typically recommend the service to couples), but the ultimate decision maker will probably be a female (the wife of the couple that will attend the retreat).

Industry/Entity Type

Counseling

Font styles to use
Serif
Sans Serif
Other font styles liked:
• Audrey

Colors

Designer to choose colors to be used in the design.

Requirements
Must have
• Logo for Brightwater Circle. Color scheme that is complementary to the tree artwork provided. Font that incorporates or complements the font in the logo - Audrey. Photo of Tom & Norma with their bio (use a placeholder for now). Please include at least one or two stock photos of married couples somewhere in the brochure. See the examples in the creative brief and please let me know if you need me to provide the actual files (if you do not have access to Kelvora Images).
Nice to have
• A design option that includes an infographic/icon style for me to consider. See creative brief document for more on this idea.
Should not have
• Note: I removed the prior instructions indicating this design should not have a full page bleed. That is no longer a limitation on this design. Feel free to go with what you think looks best to make your submission as strong as possible.

```html
<!DOCTYPE html>
<html lang="en">
<head>
<meta charset="utf-8">
<title>Brightwater Circle – Retreat Brochure</title>
<link href="https://fonts.googleapis.com/css2?family=Cormorant+Garamond:ital,wght@0,500;0,600;1,500&family=Lato:ital,wght@0,300;0,400;0,700;1,300&display=swap" rel="stylesheet">
<style>
:root{
  --bg:#d5d6d8;
  --paper:#ffffff;
  --olive:#a4b36a;
  --olive-dark:#7d8a45;
  --emerald:#2a9a68;
  --emerald-dark:#1c7a50;
  --text:#3a3a3a;
  --heading:#5b5230;
  --red:#e0261f;
  --green:#7fb13a;
  --orange:#f2a81d;
  --sage-text:#9cab62;
  --quote-mark:#8a9a4b;
}
*{box-sizing:border-box;margin:0;padding:0}
html,body{width:933px;height:1200px;overflow:hidden}
body{background:var(--bg);font-family:"Lato",sans-serif;font-weight:300;color:var(--text);position:relative}
.spread{position:absolute;left:75px;width:825px;height:534px;background:var(--paper);box-shadow:0 10px 14px rgba(0,0,0,.18);overflow:hidden}
.spread-top{top:23px}
.spread-bottom{top:610px}
.page{position:absolute;top:0;width:412.5px;height:534px;overflow:hidden}
.page-left{left:0}
.page-right{left:412.5px}
.abs{position:absolute}
.center{text-align:center}

/* agenda */
.agenda{left:0;top:0;width:412.5px;height:201px;background:var(--olive)}
.agenda h2{position:absolute;top:10px;width:100%;text-align:center;font-family:"Cormorant Garamond",serif;font-weight:500;font-size:17px;color:#fff;letter-spacing:.5px}
.day{position:absolute;top:35px;width:125px}
.pill{display:block;background:#fff;border-radius:8px;height:12px;line-height:12px;font-size:7px;font-weight:400;text-align:center;color:#333;width:110px}
.day ul{list-style:none;margin-top:9px}
.day li{font-size:6.6px;line-height:9.4px;color:#fff;padding-left:7px;position:relative;font-weight:300}
.day li::before{content:"";position:absolute;left:0;top:3px;width:3.5px;height:3.5px;border-radius:50%;background:#fff}
.agenda-note{position:absolute;top:186px;width:100%;text-align:center;font-size:5.6px;color:#fff}

.brand{display:flex;align-items:center;justify-content:center;gap:5px;font-family:"Cormorant Garamond",serif;font-weight:600;color:var(--heading);letter-spacing:1px}
.brand-dot{width:9px;height:9px;border-radius:50%;background:var(--olive)}

.invest-title{top:314px;width:100%;font-family:"Cormorant Garamond",serif;font-weight:600;font-size:13.5px;color:var(--heading);letter-spacing:.3px}
.body-copy{font-size:8.2px;line-height:12.8px;color:#333;font-weight:300}
.credits{top:458px;width:100%;font-size:7.8px;line-height:13.4px;color:#fff;font-weight:300}

.cover-title{top:456px;width:100%;font-family:"Cormorant Garamond",serif;font-weight:500;font-size:28px;color:#fff;letter-spacing:1px}
.cover-sub{top:491px;width:100%;font-size:12.2px;color:#b9dc9c;font-weight:300;letter-spacing:.2px}
.cover-tag{top:508px;width:100%;font-family:"Cormorant Garamond",serif;font-style:italic;font-size:11px;color:#fff}

/* inner spread */
.risk-title{top:211px;width:100%;font-family:"Cormorant Garamond",serif;font-weight:600;font-size:13.5px;color:var(--heading)}
.stat{left:16px;height:10px}
.stat-text{font-size:7.2px;color:#333}
.retreat-sub{top:306px;width:100%;font-family:"Cormorant Garamond",serif;font-style:italic;font-weight:500;font-size:12px;color:var(--sage-text)}
.invite{left:15px;top:355px;width:383px;height:104px;border-radius:6px;background:linear-gradient(135deg,#2e9d6a,#1f8a59 60%,#2aa06c)}
.invite h3{position:absolute;top:8px;width:100%;text-align:center;font-family:"Cormorant Garamond",serif;font-weight:500;font-size:12.5px;color:#fff}
.invite .lead{position:absolute;top:27px;width:100%;text-align:center;font-size:8px;line-height:10px;color:#fff}
.goal{position:absolute;top:60px;width:108px;text-align:center}
.goal .pill{width:108px;font-size:6.8px}
.goal p{margin-top:3px;font-size:6.8px;line-height:9.2px;color:#fff}
.plus{position:absolute;top:62px;font-size:8px;color:#fff}

.hosts-title{top:197px;width:100%;font-family:"Cormorant Garamond",serif;font-weight:600;font-size:13.5px;color:var(--heading)}
.hosts-bio{left:12px;top:220px;width:389px;font-size:7.3px;line-height:10.8px;text-align:justify;color:#333}
.exp-title{top:294px;width:100%;font-family:"Cormorant Garamond",serif;font-weight:600;font-size:12px;color:var(--heading)}
.quote{position:absolute;width:186px;height:55px;border:1px solid #b9b48f;border-radius:3px;padding:8px 5px 3px}
.quote p{font-size:5.6px;line-height:7.9px;font-style:italic;color:#555;text-align:justify}
.qmark{position:absolute;top:-11px;left:76px;width:32px;height:16px;background:#fff;text-align:center;font-family:"Cormorant Garamond",serif;font-weight:600;font-size:32px;line-height:30px;color:var(--quote-mark);overflow:hidden}
.strip{left:0;top:522px;width:412.5px;height:12px;background:var(--olive)}
.fold{position:absolute;left:411px;top:0;width:3px;height:534px;background:linear-gradient(90deg,rgba(0,0,0,.05),rgba(0,0,0,.12),rgba(0,0,0,.03))}
</style>
</head>
<body>

<section class="spread spread-top">
  <div class="page page-left">
    <div class="abs agenda">
      <h2>AGENDA</h2>
      <div class="day" style="left:16px">
        <span class="pill">Day One</span>
        <ul>
          <li>Arrive, settle in, get acquainted</li>
          <li>Individual reflection and<br>couple connection</li>
          <li>Lunch</li>
          <li>Session 1*</li>
          <li>Break</li>
          <li>Session 2</li>
          <li>Free time</li>
          <li>Dinner</li>
          <li>5 minute huddle</li>
        </ul>
      </div>
      <div class="day" style="left:148px">
        <span class="pill">Day Two</span>
        <ul>
          <li>Coffee, individual reflection,<br>time with God</li>
          <li>Breakfast</li>
          <li>Couple breakout</li>
          <li>Session 3</li>
          <li>Break</li>
          <li>Lunch</li>
          <li>Session 4: Building Bridges part 1</li>
          <li>Break</li>
          <li>Session 5: Building Bridges part 2</li>
          <li>Free time</li>
          <li>Dinner date (couple only)</li>
          <li>5 minute huddle</li>
        </ul>
      </div>
      <div class="day" style="left:280px">
        <span class="pill">Day Three</span>
        <ul>
          <li>Coffee, individual reflection<br>and time with God</li>
          <li>Breakfast</li>
          <li>Session 6: Integrated Intimacy</li>
          <li>Lunch</li>
          <li>Session 7</li>
          <li>Break</li>
          <li>Wrap up, next steps</li>
          <li>Pray</li>
          <li>Depart</li>
        </ul>
      </div>
      <p class="agenda-note">* Each session lasts approximately 2 hours and includes time with the hosts and breakouts for reflection and exercises.</p>
    </div>

    <div class="abs brand" style="top:258px;width:100%;font-size:15px"><span class="brand-dot"></span>BRIGHTWATER CIRCLE</div>

    <h2 class="abs invest-title center">READY TO INVEST IN YOUR MARRIAGE?</h2>
    <p class="abs body-copy center" style="top:339px;width:100%">Contact Tom &amp; Norma Halden to request a confidential initial consultation:<br><strong style="font-weight:700">info@brightwatercircleretreat.com</strong></p>
    <p class="abs body-copy center" style="top:378px;width:100%">Retreat expenses are covered for you – including meals, lodging, teaching and materials.<br>Couples are responsible for their own transportation to the retreat and childcare, if needed.<br>Additional scholarships are available.</p>

    <svg class="abs" style="left:0;top:425px" width="412.5" height="109" viewBox="0 0 412.5 109" aria-hidden="true">
      <defs><linearGradient id="em1" x1="0" y1="0" x2="1" y2="1"><stop offset="0" stop-color="#1f8a57"/><stop offset=".6" stop-color="#2c9e6b"/><stop offset="1" stop-color="#24905f"/></linearGradient></defs>
      <path d="M0 20 Q200 0 412.5 2 L412.5 109 L0 109Z" fill="#a4b36a"/>
      <path d="M0 26 Q200 7 412.5 8 L412.5 109 L0 109Z" fill="url(#em1)"/>
    </svg>
    <p class="abs credits center">The Hollis Institute, 2006<br>The Marlow Group, Clergy Home Life Survey, 2016<br>Testimonials have been edited for clarity and confidentiality.<br>© Tom and Norma Halden. Tree artwork by Ada Ferrin.</p>
  </div>

  <div class="page page-right">
    <div class="abs brand" style="top:60px;width:100%;font-size:17px"><span class="brand-dot"></span>BRIGHTWATER CIRCLE</div>
    <div class="abs" role="img" aria-label="Photo of a couple embracing on a hillside above a lake at sunset" style="left:0;top:150px;width:412.5px;height:300px;background:linear-gradient(160deg,#e9ecea 0%,#c5b79c 30%,#8e7a5d 55%,#6f7a5b 75%,#a9925f 100%)"></div>
    <svg class="abs" style="left:0;top:90px" width="412.5" height="100" viewBox="0 0 412.5 100" aria-hidden="true">
      <path d="M0 0 Q150 70 412.5 72 L412.5 0Z" fill="#fff"/>
      <path d="M0 4 Q150 64 412.5 74 L412.5 69 Q150 58 0 -2Z" fill="#a4b36a"/>
      <path d="M0 12 Q150 70 412.5 79 L412.5 75 Q150 66 0 8Z" fill="#fff" opacity=".9"/>
    </svg>
    <svg class="abs" style="left:0;top:425px" width="412.5" height="109" viewBox="0 0 412.5 109" aria-hidden="true">
      <defs><linearGradient id="em2" x1="0" y1="0" x2="1" y2="1"><stop offset="0" stop-color="#24925f"/><stop offset=".5" stop-color="#2ea36e"/><stop offset="1" stop-color="#1e8656"/></linearGradient></defs>
      <path d="M0 2 Q200 -2 412.5 20 L412.5 109 L0 109Z" fill="#a4b36a"/>
      <path d="M0 8 Q200 4 412.5 27 L412.5 109 L0 109Z" fill="url(#em2)"/>
    </svg>
    <h1 class="abs cover-title center">BRIGHTWATER CIRCLE</h1>
    <p class="abs cover-sub center">CULTIVATE A LIFE-GIVING RELATIONSHIP FOR ALL SEASONS</p>
    <p class="abs cover-tag center">A Personalized Retreat for Couples in Ministry</p>
  </div>
  <div class="fold"></div>
</section>

<section class="spread spread-bottom">
  <div class="page page-left">
    <div class="abs" role="img" aria-label="Photo of a city river lined with skyscrapers at sunset, a boat on the water" style="left:0;top:0;width:412.5px;height:195px;background:linear-gradient(180deg,#b9c9d8 0%,#8a97a5 35%,#6f6b62 60%,#2f6b6a 80%,#1f4f52 100%)"></div>
    <svg class="abs" style="left:0;top:160px" width="412.5" height="45" viewBox="0 0 412.5 45" aria-hidden="true">
      <path d="M0 30 Q200 -5 412.5 0 L412.5 45 L0 45Z" fill="#7d8a45"/>
      <path d="M0 36 Q200 4 412.5 6 L412.5 45 L0 45Z" fill="#fff"/>
    </svg>
    <h2 class="abs risk-title center">MINISTRY MARRIAGES ARE AT RISK</h2>
    <div class="abs stat" style="top:242px;width:71px;background:var(--red)"></div>
    <div class="abs stat" style="top:261px;width:55px;background:var(--green)"></div>
    <div class="abs stat" style="top:280px;width:40px;background:var(--orange)"></div>
    <p class="abs stat-text" style="left:98px;top:243px"><span style="color:var(--red)">77%</span> of pastors feel they do not have a good marriage</p>
    <p class="abs stat-text" style="left:98px;top:262px"><span style="color:var(--green)">48%</span> say their current ministry role has been difficult on their marriage</p>
    <p class="abs stat-text" style="left:98px;top:281px"><span style="color:var(--orange)">26%</span> of pastors face significant marital problems</p>
    <h3 class="abs retreat-sub center">A retreat for couples in ministry</h3>
    <p class="abs center" style="top:324px;width:100%;font-size:7.4px;color:#333">Brightwater Circle retreats provide you time, space, and Bible-based tools to cultivate a life-giving marriage.</p>

    <div class="abs invite">
      <h3>YOUR INVITATION</h3>
      <p class="lead">Whether your marriage is thriving, in distress, or needs a fresh start, Brightwater Circle<br>retreats equip couples in ministry to:</p>
      <div class="goal" style="left:7px"><span class="pill">Deepen Intimacy</span><p>Reinvigorate love by<br>being heard and valued</p></div>
      <span class="plus" style="left:119px">+</span>
      <div class="goal" style="left:138px"><span class="pill">Untangle Relational Knots</span><p>Heal hurts, care for yourself<br>and each other with grace</p></div>
      <span class="plus" style="left:250px">+</span>
      <div class="goal" style="left:269px"><span class="pill">Replenish Joy</span><p>Create an environment to<br>grow and rediscover fun</p></div>
    </div>

    <p class="abs center" style="top:469px;width:100%;font-size:7.5px;line-height:10.6px;color:#333">The 3-day retreat is personally tailored for one couple only. We provide a lovely, comfortable, private<br>and safe setting where everything is taken care of. We can welcome you to our locations in Austin and<br>Chicago or – in special circumstances –bring the retreat to your area.</p>
    <div class="abs strip"></div>
  </div>

  <div class="page page-right">
    <div class="abs" role="img" aria-label="Photo of a smiling couple embracing on a busy city street with soap bubbles" style="left:0;top:0;width:412.5px;height:175px;background:linear-gradient(120deg,#5a4a3e 0%,#9a8672 35%,#d9d2c6 55%,#7d6e62 80%,#3e3a38 100%)"></div>
    <svg class="abs" style="left:0;top:140px" width="412.5" height="50" viewBox="0 0 412.5 50" aria-hidden="true">
      <path d="M0 22 Q200 -2 412.5 25 L412.5 50 L0 50Z" fill="#7d8a45"/>
      <path d="M0 27 Q200 4 412.5 32 L412.5 50 L0 50Z" fill="#fff"/>
    </svg>
    <div class="abs" style="left:286px;top:108px;width:104px;height:104px;border-radius:50%;background:#e6e6e6"></div>
    <div class="abs" role="img" aria-label="Placeholder photo of hosts Tom and Norma" style="left:292px;top:114px;width:92px;height:92px;border-radius:50%;background:linear-gradient(160deg,#b7d4e6,#9fb7a0 60%,#6f8a6a)"></div>

    <h2 class="abs hosts-title center">YOUR HOSTS</h2>
    <p class="abs hosts-bio">Tom and Norma Halden bring more than 20 years of experience helping build and restore Christ-centered marriages. They have experienced God’s redemption in their own broken stories. A compassionate and insightful listener, Tom is a retired energy industry leader currently serving on a corporate board and church overseer board. Norma formerly served in full-time ministry and is a gifted teacher who delights in unpacking God’s truth. God has used the time and tools they offer to transform many marriages.</p>
    <h3 class="abs exp-title center">Experience transformation</h3>

    <div class="quote" style="left:12px;top:326px"><span class="qmark">“</span><p>Our marriage was in crisis. The stress of ministry had taken a deep toll on us and in the worst moments we didn’t even like each other anymore. Tom and Norma are people we trust with the darkest moments of our lives. They stood with us and held up our arms to allow us to continue.</p></div>
    <div class="quote" style="left:211px;top:326px"><span class="qmark">“</span><p>Tom and Norma meet people in their pain and brokenness without shame or judgment and gently help them make major shifts from a place of extreme distress to a hopeful and productive path forward.</p></div>
    <div class="quote" style="left:12px;top:392px"><span class="qmark">“</span><p>During a critical time, Tom and Norma helped us navigate our marriage around the traps that we so easily and repeatedly fell into… We were sitting ducks for the evil one… They took us to the deep end of the marriage pool and dove in first. I see a more fruitful and God honoring marriage ahead.</p></div>
    <div class="quote" style="left:211px;top:392px"><span class="qmark">“</span><p>Tom and Norma understand the sanctity of safely and compassionately learning from each other’s stories…the triumphs, the failures, the times of healing, and the times of deep woundedness. They hold the stories of the couples they work tenderly, confidentially and dearly.</p></div>
    <div class="quote" style="left:12px;top:458px"><span class="qmark">“</span><p>This experience was the most important thing I have ever done in my life outside of saying yes to Jesus. As a pastor, I have always known that my family is my number one ministry. This experience helped me take that theoretical goal and turn it into a reality.</p></div>
    <div class="quote" style="left:211px;top:458px"><span class="qmark">“</span><p>Tom and Norma exemplify these qualities: a safety zone with in-the-vault assurance, advice grounded in scripture, a straightforward message, truth spoken in love even when painful, vulnerability and authenticity.</p></div>
    <div class="abs strip"></div>
  </div>
  <div class="fold"></div>
</section>

</body>
</html>
```